TV - business card

Tidewell Vantage is an insurance brokerage firm, inovative, proactive, vigorous, which aims to become the leader of the insurance brokers in Anfrica. We should like to get some designs which should be avoided also in Gray / Metallic for the Administration and Orange / Blue for the Managers (ike in the picture sent). The Blue / Green logo is not the correct one, but the source of the file. Please adjust the color accordingly for the business cards. 1 / Orange / Blue 2 / Gray / Metallic We want something classic but which is transmitted strenght, inovation, modernity and most of all, rapidity. We want something start-up like, very punchy and catching eye remaining profesional at the same time. Name: Delton Ashgrove Function: Managing Director Address: N ° 73/74 Cmt. Bolembe - R / C 2B Esquerda - Bairro Quimbuta - Luanda Tel: (+244) 947 385 619 Email: delton.ashgrove@tidewell-v.com Website: www.tidewell-v. com We want classic in the front and creative, colorfull at the back. The cards will be printed in relief, with very high quality of paper.
Industry/Entity Type
Insurance Broker
Colors
Designer to choose colors to be used in the design.
Look and feel

```html
<!DOCTYPE html>
<html lang="en">
<head>
<meta charset="utf-8">
<title>Tidewell Vantage – Business Card</title>
<link rel="stylesheet" href="https://fonts.googleapis.com/css2?family=Roboto+Condensed:wght@700&family=Montserrat:wght@400;500&display=swap">
<style>
  :root {
    --page: #e9ecef;
    --orange: #e8692a;
    --orange-red: #e4473a;
    --blue: #2a78c4;
    --blue-light: #3f8fd6;
    --blue-deep: #1f66b0;
    --paper: #f6f6f4;
    --white: #ffffff;
  }
  * { margin: 0; padding: 0; box-sizing: border-box; }
  html, body { width: 1200px; height: 800px; overflow: hidden; background: var(--page); }
  .canvas {
    width: 1200px; height: 800px;
    display: flex; align-items: center; justify-content: center; gap: 40px;
  }
  .card {
    position: relative; width: 540px; height: 308px;
    background: var(--paper); overflow: hidden;
    box-shadow: 0 18px 40px rgba(0,0,0,.18), 0 3px 8px rgba(0,0,0,.12);
  }
  .card__shapes { position: absolute; inset: 0; width: 100%; height: 100%; }

  .wordmark {
    position: absolute; display: flex; align-items: center; gap: 12px;
    font-family: "Roboto Condensed", "Arial Narrow", sans-serif;
    font-weight: 700; color: var(--blue); text-transform: uppercase;
    letter-spacing: .04em; line-height: 1;
  }
  .wordmark__dot { border-radius: 50%; background: var(--orange); flex: none; }

  .card--back .wordmark { left: 250px; top: 160px; font-size: 30px; }
  .card--back .wordmark__dot { width: 26px; height: 26px; }

  .card--front .wordmark {
    left: 398px; top: 170px; font-size: 17px; flex-direction: column;
    align-items: center; gap: 8px; text-align: center; width: 134px;
  }
  .card--front .wordmark__dot { width: 16px; height: 16px; }

  .holder {
    position: absolute; left: 34px; top: 36px;
    font-family: "Roboto Condensed", "Arial Narrow", sans-serif;
    font-weight: 700; font-size: 28px; color: var(--white); letter-spacing: -.01em;
  }
  .contacts {
    position: absolute; left: 34px; top: 128px; list-style: none;
    font-family: "Montserrat", Arial, sans-serif; font-size: 11px; color: var(--white);
  }
  .contacts li { display: flex; align-items: flex-start; gap: 9px; margin-bottom: 8px; line-height: 1.35; }
  .contacts svg { width: 12px; height: 12px; flex: none; margin-top: 1px; fill: var(--white); }
</style>
</head>
<body>
<main class="canvas">

  <!-- Card front: brand side -->
  <section class="card card--back" aria-label="Card side with company name">
    <svg class="card__shapes" viewBox="0 0 540 308" preserveAspectRatio="none" aria-hidden="true">
      <defs>
        <linearGradient id="backOrange" x1="0" y1="0" x2="1" y2="1">
          <stop offset="0" stop-color="#ec7128"/>
          <stop offset="1" stop-color="#e4503a"/>
        </linearGradient>
      </defs>
      <rect width="540" height="308" fill="var(--paper)"/>
      <polygon points="0,0 330,0 0,110" fill="url(#backOrange)"/>
      <polygon points="0,110 330,0 540,0 540,40 150,72 290,308 0,308" fill="var(--blue)"/>
      <polygon points="150,72 540,40 540,0 430,0" fill="var(--blue-light)"/>
      <polygon points="0,170 150,72 290,308 225,308" fill="var(--blue-deep)"/>
      <polygon points="0,110 330,0 200,40 0,150" fill="var(--blue-light)" opacity=".55"/>
      <polygon points="150,72 540,40 540,308 290,308" fill="var(--paper)"/>
    </svg>
    <div class="wordmark"><span class="wordmark__dot"></span><span>Tidewell Vantage</span></div>
  </section>

  <!-- Card back: contact side -->
  <section class="card card--front" aria-label="Card side with contact details">
    <svg class="card__shapes" viewBox="0 0 540 308" preserveAspectRatio="none" aria-hidden="true">
      <defs>
        <linearGradient id="frontOrange" x1="0" y1="0" x2="1" y2="1">
          <stop offset="0" stop-color="#ec7128"/>
          <stop offset="1" stop-color="#e4473a"/>
        </linearGradient>
      </defs>
      <rect width="540" height="308" fill="url(#frontOrange)"/>
      <polygon points="300,0 540,0 540,60 395,100 380,308 345,308" fill="var(--blue)"/>
      <polygon points="300,0 395,100 540,60 540,0" fill="var(--blue-light)"/>
      <polygon points="300,0 395,100 345,308 330,200" fill="var(--blue-deep)"/>
      <polygon points="395,100 540,60 540,308 380,308" fill="var(--paper)"/>
    </svg>

    <h1 class="holder">Delton Ashgrove</h1>

    <ul class="contacts">
      <li>
        <svg viewBox="0 0 24 24" aria-hidden="true"><path d="M6.6 10.8a15.1 15.1 0 0 0 6.6 6.6l2.2-2.2a1 1 0 0 1 1-.25 11.4 11.4 0 0 0 3.6.57 1 1 0 0 1 1 1V20a1 1 0 0 1-1 1A17 17 0 0 1 3 4a1 1 0 0 1 1-1h3.5a1 1 0 0 1 1 1c0 1.25.2 2.45.57 3.57a1 1 0 0 1-.25 1z"/></svg>
        <span>(+244) 947 385 619</span>
      </li>
      <li>
        <svg viewBox="0 0 24 24" aria-hidden="true"><path d="M2 5h20v14H2z M2 5l10 8 10-8" fill="none" stroke="#fff" stroke-width="2"/></svg>
        <span>delton.ashgrove@tidewell-v.com</span>
      </li>
      <li>
        <svg viewBox="0 0 24 24" aria-hidden="true"><g fill="none" stroke="#fff" stroke-width="2"><circle cx="12" cy="12" r="9.5"/><ellipse cx="12" cy="12" rx="4" ry="9.5"/><path d="M2.5 12h19"/></g></svg>
        <span>www.tidewell-v. com</span>
      </li>
      <li>
        <svg viewBox="0 0 24 24" aria-hidden="true"><path d="M12 2a7 7 0 0 0-7 7c0 5.2 7 13 7 13s7-7.8 7-13a7 7 0 0 0-7-7zm0 9.5A2.5 2.5 0 1 1 12 6.5a2.5 2.5 0 0 1 0 5z"/></svg>
        <span>N ° 73/74 Cmt. Bolembe - R / C 2B Esquerda -<br>Bairro Quimbuta - Luanda</span>
      </li>
    </ul>

    <div class="wordmark"><span class="wordmark__dot"></span><span>Tidewell Vantage</span></div>
  </section>

</main>
</body>
</html>
```